Brightwell Cleaning Services - Redesign

I've got my website designed a few years ago and it looks dated now. I would like to get a modern, happy, bright, and clean look. All the content needed can be found at my current website www.brightwellhq.example. Not necessarily need to use all of it, since I want something more clean and easy to read.
I need a 5 pages website:
HOME | SERVICES | ESTIMATE |TESTIMONIALS | CONTACT US

Industry/Entity Type

Janitorial Service

Number of Pages Required

5+ page

Colors
0792cd
34a6d7
85cae6
cee9f5
ebebeb
f0f0f0
f5f5f5
b1b1b1
000000

Requirements
Must have
• Who we are?
• Brightwell Cleaning Services is a local, family-owned, client-focused house and office cleaning company that strives to ensure the highest level of customer satisfaction. We offer expert residential and commercial cleaning services to all the Seattle and Eastside areas.
• Why Brightwell?
• √ We are insured, bonded and licensed.
•  Brightwell Cleaning Service is Fully Insured so you can rest easy knowing your home is protected.
•  Copy of insurance available upon request.
•

√ We provide all supplies and equipments needed to thoroughly clean your home or business.

• √ We are not a franchise. We are a local, family-owned company.

• When you call Brightwell Cleaning Services, you’ll always speak to one of the owners, which is a great benefit to you since this allows us to give you the personal attention and more time needed to clean your home the way you want it cleaned.

• √ We are good at what we do, and we like doing it.

```html
<!DOCTYPE html>
<html lang="en">
<head>
<meta charset="utf-8">
<title>Brightwell Cleaning Services</title>
<link href="https://fonts.googleapis.com/css2?family=Montserrat:wght@400;500;600&family=Open+Sans:wght@400;600&family=Dancing+Script:wght@500&display=swap" rel="stylesheet">
<style>
:root{
  --blue-deep:#0792cd;
  --blue:#34a6d7;
  --blue-light:#85cae6;
  --blue-pale:#cee9f5;
  --grey-1:#ebebeb;
  --grey-2:#f0f0f0;
  --grey-3:#f5f5f5;
  --grey-mid:#b1b1b1;
  --black:#000000;
  --footer:#2b2b2b;
  --white:#ffffff;
  --text:#3a3a3a;
}
*{margin:0;padding:0;box-sizing:border-box}
html,body{width:1200px;height:3025px;overflow:hidden;background:var(--white)}
body{font-family:"Open Sans",Arial,sans-serif;color:var(--text)}
.page{position:relative;width:1200px;height:3025px;overflow:hidden}
.abs{position:absolute}

/* hero */
.hero-photo{left:0;top:0;width:1200px;height:700px;
  background:linear-gradient(120deg,var(--grey-3) 0%,var(--white) 35%,var(--blue-pale) 70%,var(--grey-2) 100%)}
.hero-cut{left:0;top:560px;width:1200px;height:160px}
.main-nav{left:0;top:30px;width:1200px;display:flex;justify-content:center;gap:0}
.main-nav a{font-family:"Open Sans",Arial,sans-serif;font-weight:600;font-size:17px;color:var(--blue-deep);text-decoration:none;padding:0 24px;position:relative}
.main-nav a.current::before{content:"";position:absolute;left:50%;top:-12px;width:34px;height:10px;margin-left:-17px;
  border-top:2px solid var(--blue-deep);border-left:2px solid var(--blue-deep);transform:skewX(0);clip-path:polygon(0 100%,50% 0,100% 100%,100% 0,0 0);}
.brand{left:0;top:270px;width:1200px;text-align:center;font-family:"Montserrat",sans-serif;font-weight:600;font-size:48px;color:var(--blue-deep);letter-spacing:1px}

.intro-title{left:0;top:664px;width:1200px;text-align:center;font-family:"Montserrat",sans-serif;font-weight:400;font-size:40px;color:var(--black)}
.intro-title span{color:var(--blue)}
.script{font-family:"Dancing Script",cursive;font-weight:500}
.intro-sub{left:0;top:712px;width:1200px;text-align:center;font-size:20px;color:#333}
.intro-text{left:0;top:758px;width:1200px;text-align:center;font-size:15px;color:#555}
.mascot{left:404px;top:835px;width:322px;height:150px;border-radius:70px 70px 0 0;
  background:linear-gradient(180deg,var(--blue-pale),var(--blue-light))}

/* service bands */
.band{left:0;width:1200px}
.band-blue{background:linear-gradient(135deg,var(--blue) 0%,#3fb0e0 55%,var(--blue-light) 100%)}
.band-grey{background:linear-gradient(135deg,var(--grey-3) 0%,var(--grey-1) 50%,#d9dde0 100%)}
.band-school{background:linear-gradient(180deg,#dfe7e8 0%,var(--grey-2) 45%,#e6ddd3 100%)}
.svc{width:560px}
.svc h2{font-family:"Montserrat",sans-serif;font-weight:500;font-size:23px;letter-spacing:1px;margin-bottom:12px}
.svc p{font-size:14.5px;line-height:22px;margin-bottom:22px}
.svc-light h2,.svc-light p{color:var(--white)}
.svc-dark h2{color:var(--blue-deep)}
.svc-dark p{color:#333}
.svc .tagline{font-family:"Montserrat",sans-serif;font-weight:500;font-size:20px;color:var(--white)}
.badge{width:230px;height:230px;border-radius:50%;background:var(--white);display:flex;align-items:center;justify-content:center}
.badge-inner{width:204px;height:204px;border-radius:50%;background:var(--blue-deep);display:flex;align-items:center;justify-content:center}

/* testimonials */
.clients-title{left:0;top:2540px;width:1200px;text-align:center;font-family:"Montserrat",sans-serif;font-size:36px;color:var(--white)}
.clients-title strong{font-weight:500;color:var(--black)}
.clients-sub{left:0;top:2584px;width:1200px;text-align:center;font-size:19px;color:var(--black)}
.quote{left:236px;top:2646px;width:728px;height:100px;background:var(--white);border-radius:4px;
  font-size:14.5px;line-height:23px;color:#444;text-align:center;padding:16px 40px}
.quote::after{content:"";position:absolute;left:50%;bottom:-14px;margin-left:-14px;border:14px solid transparent;border-bottom:0;border-top-color:var(--white)}
.quote-name{left:0;top:2780px;width:1200px;text-align:center;font-family:"Montserrat",sans-serif;font-size:25px;color:var(--white)}
.quote-name em{font-family:"Open Sans",Arial,sans-serif;font-size:18px}

/* footer */
.site-footer{left:0;top:2905px;width:1200px;height:120px;background:var(--footer)}
.foot-nav{left:60px;top:2937px;display:flex}
.foot-nav a{color:var(--white);font-size:14px;text-decoration:none;padding:0 18px;border-left:1px solid #555}
.foot-nav a:first-child{padding-left:18px;border-left:0}
.copyright{left:78px;top:2976px;font-size:13.5px;color:var(--white)}
.copyright span{color:var(--blue)}
.foot-brand{left:920px;top:2934px;font-family:"Montserrat",sans-serif;font-weight:600;font-size:42px;color:var(--grey-mid)}
</style>
</head>
<body>
<div class="page">

  <div class="abs hero-photo" role="img" aria-label="Photo of a smiling cleaner wiping a kitchen cabinet in a bright white room"></div>
  <svg class="abs hero-cut" viewBox="0 0 1200 160" preserveAspectRatio="none" aria-hidden="true">
    <polygon points="0,90 520,110 1200,40 1200,160 0,160" fill="#ffffff"/>
  </svg>

  <nav class="abs main-nav">
    <a href="#">HOME</a>
    <a href="#" class="current">SERVICES</a>
    <a href="#">ESTIMATE</a>
    <a href="#">TESTIMONIALS</a>
    <a href="#">CONTACT US</a>
  </nav>

  <div class="abs brand">Brightwell Cleaning Services</div>

  <h1 class="abs intro-title">Commercial &amp; Residential <span>Cleaning Services</span></h1>
  <div class="abs intro-sub script">Services</div>
  <p class="abs intro-text">Brightwell Cleaning Services specializes in House Cleaning and Janitorial Services for your home or place of business!</p>

  <div class="abs mascot" role="img" aria-label="Smiling cleaner in blue gloves leaning over the section edge"></div>

  <!-- residential -->
  <section class="abs band band-blue" style="top:978px;height:486px" role="img" aria-label="Bright living room photo under blue tint"></section>
  <div class="abs svc svc-light" style="left:80px;top:1078px">
    <h2>RESIDENTIAL CLEANING</h2>
    <p>Brightwell Cleaning Services offer top quality homes and apartments cleaning services within Seattle, Redmond, Kirkland, Bothell, Sammamish, Issaquah, Woodinville, Medina, Mercer Island, Renton. When it comes to hire residential home cleaning services, you can count on Brightwell Cleaning Services.</p>
    <p>We provide the healthiest, most thorough professional house cleaning services available. We pride ourselves on going above and beyond what other cleaners offer to provide you with a home that is clean and shines from ceiling to floor, bathroom to kitchen. Our aim is to provide our residential with top quality cleaning services at an affordable rate.</p>
  </div>
  <div class="abs badge" style="left:777px;top:1055px"><div class="badge-inner">
    <svg width="120" height="80" viewBox="0 0 120 80" aria-hidden="true">
      <polygon points="4,42 40,10 76,42 66,42 66,70 14,70 14,42" fill="#fff"/>
      <polygon points="54,44 82,22 116,50 108,50 108,70 64,70" fill="#fff"/>
      <polygon points="40,22 60,40 20,40" fill="#0792cd"/>
    </svg>
  </div></div>

  <!-- office -->
  <section class="abs band band-grey" style="top:1466px;height:330px" role="img" aria-label="Photo of an empty modern office with desks and chairs"></section>
  <div class="abs badge" style="left:198px;top:1513px"><div class="badge-inner">
    <svg width="110" height="110" viewBox="0 0 110 110" aria-hidden="true">
      <polygon points="20,100 20,40 45,30 45,100" fill="#fff"/>
      <polygon points="50,100 50,10 75,25 75,100" fill="#fff"/>
      <polygon points="80,100 80,50 95,58 95,100" fill="#fff"/>
    </svg>
  </div></div>
  <div class="abs svc svc-dark" style="left:555px;top:1547px">
    <h2>OFFICE CLEANING</h2>
    <p>We clean large or small office buildings, medical clinics/facilities, banks, department and retail stores, government facilities, condos, apartments, single and multi family homes and much more.</p>
    <p>Contact us today for additional details. BCS maintains the highest and finest details of excellent cleaning services.</p>
  </div>

  <!-- move out / in -->
  <section class="abs band band-blue" style="top:1796px;height:338px"></section>
  <div class="abs svc svc-light" style="left:80px;top:1882px">
    <h2>MOVE OUT/IN CLEANING</h2>
    <p>Are planning on selling your property, Or your tenancy agreement come to an end? Then this service is especially design for you. We know how important is to leave the property in clean and in good condition.</p>
    <p>We would be glad to clean and maintain your property for you. We can ensure your new home, or office space is sparkling clean, flawless and ready for occupancy</p>
    <div class="tagline">We want to be your cleaning partner.</div>
  </div>
  <div class="abs badge" style="left:777px;top:1833px"><div class="badge-inner">
    <svg width="120" height="80" viewBox="0 0 120 80" aria-hidden="true">
      <polygon points="4,42 40,10 76,42 66,42 66,70 14,70 14,42" fill="#fff"/>
      <polygon points="54,44 82,22 116,50 108,50 108,70 64,70" fill="#fff"/>
    </svg>
  </div></div>

  <!-- school -->
  <section class="abs band band-school" style="top:2136px;height:420px" role="img" aria-label="Photo of a classroom with desks and a green board"></section>
  <div class="abs badge" style="left:198px;top:2164px"><div class="badge-inner">
    <svg width="110" height="110" viewBox="0 0 110 110" aria-hidden="true">
      <polygon points="20,100 20,25 70,10 70,100" fill="#fff"/>
      <polygon points="72,100 72,35 95,45 95,100" fill="#fff"/>
      <g stroke="#0792cd" stroke-width="4">
        <line x1="20" y1="40" x2="70" y2="32"/><line x1="20" y1="55" x2="70" y2="50"/>
        <line x1="20" y1="70" x2="70" y2="67"/><line x1="20" y1="85" x2="70" y2="84"/>
      </g>
    </svg>
  </div></div>
  <div class="abs svc svc-dark" style="left:555px;top:2215px">
    <h2>SCHOOL/DAYCARE CLEANING</h2>
    <p>BCS is capable of tracking recess project work in a timely fashion. From floor waxing to classroom painting, your facility will always maintain the highest standard.</p>
    <p>We realize your facility is special and we are prepared to meet your unique needs. Our team of professional cleaners can implement the appropriate procedures for maintaining your property. Put our experiences in using the latest in cleaning technology to work to reduce your housekeeping budget while improving quality.</p>
  </div>

  <!-- testimonials -->
  <svg class="abs" style="left:0;top:2450px" width="1200" height="455" viewBox="0 0 1200 455" role="img" aria-label="Blue backdrop over a grid of client portrait photos">
    <polygon points="0,95 600,8 1200,95 1200,455 0,455" fill="#34a6d7"/>
    <polyline points="0,98 600,10 1200,98" fill="none" stroke="#000" stroke-width="14"/>
  </svg>
  <h2 class="abs clients-title"><strong>WHAT</strong> CLIENTS</h2>
  <div class="abs clients-sub script">Say About Us</div>
  <blockquote class="abs quote">"The folks at Brightwell are congenial and very personable, yet at the same time very professional. They keep their appointments, and they clean thoroughly and efficiently. Brightwell has been a real blessing to our family!"</blockquote>
  <div class="abs quote-name">Dana R., <em>Redmond-WA (Lakeview)</em></div>

  <!-- footer -->
  <footer class="abs site-footer"></footer>
  <nav class="abs foot-nav">
    <a href="#">HOME</a><a href="#">SERVICES</a><a href="#">ESTIMATE</a><a href="#">TESTIMONIALS</a><a href="#">CONTACT US</a>
  </nav>
  <p class="abs copyright">© <span>BRIGHTWELL CLEANING SERVICES</span> - 2016, All rights reserved</p>
  <div class="abs foot-brand">Brightwell</div>

</div>
</body>
</html>
```